Brookvale drinking water Label.

I want Drinking water label that stands out from the rest..Elegant Attractive and visible label design. Brand name is 'BROOKVALE'.

Target Market(s)

KENYA.

Industry/Entity Type

Water Company

Requirements
Must have
• Must be unique. Must be elegant and have vibrant and eye catching color.
Nice to have
• Clear or colored background with water like effects.
Should not have
• Should not have more that 4 colors.

```html
<!DOCTYPE html>
<html lang="en">
<head>
<meta charset="utf-8">
<title>Brookvale Packaged Drinking Water Label</title>
<link rel="stylesheet" href="https://fonts.googleapis.com/css2?family=Poppins:wght@400;600;700&display=swap">
<style>
  :root {
    --page: #eef1f5;
    --blue-deep: #0f1d78;
    --blue-main: #1a2fa0;
    --blue-bright: #2a8fe0;
    --aqua: #38c0ee;
    --green: #6fbf3a;
    --lime: #c6dc2c;
    --white: #ffffff;
  }
  * { box-sizing: border-box; margin: 0; padding: 0; }
  html, body { width: 1200px; height: 780px; overflow: hidden; background: var(--page); }
  .canvas {
    position: relative;
    width: 1200px;
    height: 780px;
    overflow: hidden;
    background: var(--page);
    font-family: "Poppins", sans-serif;
  }
  .label {
    position: absolute;
    left: 90px;
    top: 120px;
    width: 1020px;
    height: 540px;
    overflow: hidden;
    background: linear-gradient(180deg, var(--blue-main) 0%, var(--blue-deep) 100%);
    box-shadow: 0 14px 40px rgba(15, 29, 120, 0.18);
  }
  .label__waves { position: absolute; inset: 0; width: 100%; height: 100%; }
  .brand {
    position: absolute;
    left: 0;
    right: 0;
    top: 60px;
    display: flex;
    align-items: center;
    justify-content: center;
    gap: 22px;
  }
  .brand__dot {
    width: 46px;
    height: 46px;
    border-radius: 50%;
    background: var(--aqua);
  }
  .brand__name {
    font-weight: 700;
    font-size: 92px;
    line-height: 1;
    letter-spacing: 1px;
    color: var(--aqua);
  }
  .cert-badge {
    position: absolute;
    right: 54px;
    top: 46px;
    width: 96px;
    height: 96px;
    border-radius: 50%;
    background: var(--white);
    border: 8px solid var(--blue-main);
    box-shadow: 0 0 0 3px var(--white);
  }
  .water-band {
    position: absolute;
    left: 0;
    right: 0;
    top: 218px;
    height: 110px;
    background: linear-gradient(180deg, #3a7fdc 0%, #2256c4 45%, var(--blue-main) 100%);
  }
  .product {
    position: absolute;
    left: 0;
    right: 0;
    top: 350px;
    text-align: center;
    color: var(--white);
  }
  .product__title {
    font-weight: 600;
    font-size: 40px;
    letter-spacing: 0.5px;
  }
  .product__process {
    margin-top: 10px;
    display: flex;
    justify-content: center;
    gap: 26px;
    font-size: 20px;
    font-weight: 400;
  }
  .product__process span { display: inline-flex; align-items: center; gap: 26px; }
  .drop { width: 12px; height: 16px; }
  .volume {
    position: absolute;
    left: 40px;
    top: 424px;
    display: flex;
    flex-direction: column;
    gap: 6px;
    color: var(--lime);
    font-weight: 700;
    font-size: 24px;
  }
  .volume__icons { display: flex; gap: 8px; }
  .volume__icons svg { width: 22px; height: 22px; }
</style>
</head>
<body>
<div class="canvas">
  <section class="label">
    <svg class="label__waves" viewBox="0 0 1020 540" preserveAspectRatio="none" aria-hidden="true">
      <path d="M0 0 H300 C200 10 90 30 0 70 Z" fill="var(--green)"/>
      <path d="M0 0 H200 C130 6 60 18 0 40 Z" fill="var(--lime)"/>
      <path d="M0 470 C260 420 560 430 1020 400 V540 H0 Z" fill="var(--green)"/>
      <path d="M0 505 C300 455 640 470 1020 440 V540 H0 Z" fill="var(--lime)"/>
    </svg>

    <div class="brand">
      <span class="brand__dot"></span>
      <span class="brand__name">Brookvale</span>
    </div>
    <div class="cert-badge"></div>

    <div class="water-band" role="img" aria-label="Underwater photo with rising bubbles"></div>

    <div class="product">
      <h1 class="product__title">PACKAGED DRINKING WATER</h1>
      <p class="product__process">
        <span>OZONISED
          <svg class="drop" viewBox="0 0 12 16"><path d="M6 0 C9 5 12 8 12 11 A6 6 0 0 1 0 11 C0 8 3 5 6 0 Z" fill="var(--aqua)"/></svg>
        </span>
        <span>U.V. TREATED
          <svg class="drop" viewBox="0 0 12 16"><path d="M6 0 C9 5 12 8 12 11 A6 6 0 0 1 0 11 C0 8 3 5 6 0 Z" fill="var(--aqua)"/></svg>
        </span>
        <span>R.O. PROCESSED</span>
      </p>
    </div>

    <div class="volume">
      <div class="volume__icons">
        <svg viewBox="0 0 22 22" aria-hidden="true"><rect x="7" y="2" width="8" height="4" fill="var(--white)"/><rect x="5" y="6" width="12" height="15" rx="3" fill="var(--white)"/></svg>
        <svg viewBox="0 0 22 22" aria-hidden="true"><circle cx="11" cy="11" r="8" fill="none" stroke="var(--white)" stroke-width="2.5" stroke-dasharray="12 4"/></svg>
      </div>
      <span>500ML</span>
    </div>
  </section>
</div>
</body>
</html>
```